Private practice for psychiatry and psychotherapy needs a business card and logo

I need a logo and business card design for my private practice for psychiatry and psychotherapy. The optional names for my practice are: Voskuilen Praktijk voor Psychiatrie en Psychotherapie, or short: Praktijk Voskuilen.
I am a (child and adolescent) psychiatrist and psychotherapist. I diagnose and treat infants, children, adolescents and adults with psychiatric symptoms/disorders. I also give supervision to colleagues about their own treatments. My work is characterised by personal involvement, transparence, creativity and professionality.
I would like to have an appealing, light and bright, yet basic design that invites people (both children and adults) to contact me, gives trust and hope, without loosing professional appearance.
I uploaded my contact information which should not necessarily be all included (in this form) on the card as long as people know how to contact me. Please feel free to be creative!
Please note that my website is only temporarely and need a new design and update too!

Target Market(s)

Clients and patients (children, adolescents, adults) with psychiatric symptoms who need diagnosis and treatment. I work with private clients and patients through medical insurances.

Industry/Entity Type

Mental Health

Contact Information for Business Card

Dr. Femke Voskuilen-ter Horst
Psychiater/Kinder- en Jeugdpsychiater
Gerrit Wassinkstraat 4
3063 TW Rotterdam
t: 06-58190274
e: info@praktijkvoskuilen-voorbeeld.nl
i: www.praktijkvoskuilen-voorbeeld.nl

Logo Text

Praktijk Voskuilen voor Psychiatrie en Psychotherapie; or short: Praktijk Voskuilen

Font styles to use
Sans Serif
Other font styles liked:
• up to designer

Requirements
Must have
• Appealing, light, bright, creative, trustful, professional and unique.

```html
<!DOCTYPE html>
<html lang="nl">
<head>
<meta charset="utf-8">
<title>Praktijk Voskuilen – Visitekaartje</title>
<link href="https://fonts.googleapis.com/css2?family=Montserrat:wght@700&family=Open+Sans:wght@400&family=Roboto+Condensed:wght@400;700&display=swap" rel="stylesheet">
<style>
  :root {
    --backdrop: #2a2a2c;
    --card: #262627;
    --card-edge: #303031;
    --ink: #f2f2f2;
    --ink-soft: #cfcfcf;
    --accent: #2f8fd8;
    --accent-deep: #1d6fc0;
  }
  * { margin: 0; padding: 0; box-sizing: border-box; }
  html, body {
    width: 1200px; height: 1000px; overflow: hidden;
    background: var(--backdrop);
  }
  .stage {
    position: relative; width: 1200px; height: 1000px;
  }
  .card {
    position: absolute; left: 260px;
    width: 680px; height: 388px;
    background: var(--card);
    border: 1px solid var(--card-edge);
    box-shadow: 0 14px 30px rgba(0,0,0,.45);
  }
  .card--front { top: 70px; }
  .card--back { top: 530px; }

  .brand {
    display: flex; align-items: center; gap: 12px;
    font-family: "Montserrat", sans-serif; font-weight: 700;
    font-size: 19px; letter-spacing: .5px; color: var(--ink);
    text-transform: uppercase;
  }
  .brand__dot {
    width: 16px; height: 16px; border-radius: 50%;
    background: var(--accent);
  }
  .card--front .brand {
    position: absolute; left: 50%; top: 50%;
    transform: translate(-50%, -50%);
  }
  .card--back .brand {
    position: absolute; right: 56px; bottom: 58px;
  }

  .contact {
    position: absolute; left: 64px; top: 96px;
  }
  .contact__name {
    font-family: "Roboto Condensed", sans-serif; font-weight: 400;
    font-size: 25px; color: var(--ink); text-transform: uppercase;
    letter-spacing: .2px; line-height: 1.1;
  }
  .contact__role {
    font-family: "Roboto Condensed", sans-serif; font-weight: 700;
    font-size: 16px; color: var(--accent); margin-top: 2px;
  }
  .contact__address {
    font-family: "Open Sans", sans-serif; font-size: 17px;
    color: var(--ink-soft); margin-top: 26px; line-height: 1.25;
  }
  .contact__lines {
    list-style: none; margin-top: 20px;
    font-family: "Open Sans", sans-serif; font-size: 17px; color: var(--ink-soft);
  }
  .contact__lines li {
    display: flex; align-items: center; gap: 16px; line-height: 1.55;
  }
  .contact__lines svg { width: 14px; height: 14px; fill: var(--accent); flex: none; }
  .contact__lines .highlight { color: var(--accent); }
</style>
</head>
<body>
<main class="stage">
  <section class="card card--front" aria-label="Voorkant visitekaartje">
    <div class="brand"><span class="brand__dot"></span>Praktijk Voskuilen</div>
  </section>

  <section class="card card--back" aria-label="Achterkant visitekaartje">
    <div class="contact">
      <h1 class="contact__name">Dr. Femke Voskuilen-ter Horst</h1>
      <p class="contact__role">Psychiater/Kinder- en Jeugdpsychiater</p>
      <p class="contact__address">Gerrit Wassinkstraat 4<br>3063 TW Rotterdam</p>
      <ul class="contact__lines">
        <li>
          <svg viewBox="0 0 24 24" aria-hidden="true"><path d="M6.6 10.8a15.1 15.1 0 0 0 6.6 6.6l2.2-2.2c.3-.3.7-.4 1-.2 1.1.4 2.3.6 3.6.6.6 0 1 .4 1 1V20c0 .6-.4 1-1 1A17 17 0 0 1 3 4c0-.6.4-1 1-1h3.5c.6 0 1 .4 1 1 0 1.3.2 2.5.6 3.6.1.3 0 .7-.2 1z"/></svg>
          06-58190274
        </li>
        <li>
          <svg viewBox="0 0 24 24" aria-hidden="true"><path d="M2 5h20v14H2zM3.5 6.5l8.5 6.5 8.5-6.5v-.1H3.5z"/></svg>
          info@praktijkvoskuilen-voorbeeld.nl
        </li>
        <li>
          <svg viewBox="0 0 24 24" aria-hidden="true"><path d="M12 2a10 10 0 1 0 0 20 10 10 0 0 0 0-20zm6.9 6h-3a15 15 0 0 0-1.3-3.9A8 8 0 0 1 18.9 8zM12 4c.9 1.2 1.6 2.6 2 4h-4c.4-1.4 1.1-2.8 2-4zM4.3 14a8 8 0 0 1 0-4h3.4a16 16 0 0 0 0 4zm.8 2h3a15 15 0 0 0 1.3 3.9A8 8 0 0 1 5.1 16zm3-8h-3a8 8 0 0 1 4.3-3.9C8.8 5.3 8.4 6.6 8.1 8zM12 20c-.9-1.2-1.6-2.6-2-4h4c-.4 1.4-1.1 2.8-2 4zm2.3-6H9.7a14 14 0 0 1 0-4h4.6a14 14 0 0 1 0 4zm.3 5.9c.6-1.2 1-2.5 1.3-3.9h3a8 8 0 0 1-4.3 3.9zM16.3 14a16 16 0 0 0 0-4h3.4a8 8 0 0 1 0 4z"/></svg>
          <span>www.<span class="highlight">praktijkvoskuilen-voorbeeld</span>.nl</span>
        </li>
      </ul>
    </div>
    <div class="brand"><span class="brand__dot"></span>Praktijk Voskuilen</div>
  </section>
</main>
</body>
</html>
```